The Merry Hound - Dog Training Business Card Design

I need a business card design for a new dog training company based in Cronulla NSW called The Merry Hound. I run puppy pre school classes, adult dog classes and do one on one training in the person's home.
I have studied for 2 years and use positive reinforcement training methods based on how dogs learn. I believe in communicating with our dogs what we want them to do rather than punish them for behaviours we don't like. I would like to see designs that use the colours that are used in my logo (please see attached)
I would like a simple and classic looking design. I don't want cartoon images of dogs or any animal images or drawings on the card. I have created my logo with this mindset. I am open to the subtle use of a dog's tail, paws or paw print.

Target Market(s)

high end area which is why I want a classic looking design
adults aged 25 and over

Industry/Entity Type

Dog Training

Contact Information for Business Card

Miriam Caslett
ORBIS Trained Professional Dog Trainer
www.themerryhound-example.com.au
0499731628
miriam@themerryhound-example.com.au

Font styles to use
Sans Serif

Colors
ffffff
86cae6
757575

Requirements
Must have
• Logo - I am trying to attach my logo and colour palette but it won't allow me. I will contact the company and upload ASAP.
Should not have
• images of dogs or cartoon drawings

```html
<!DOCTYPE html>
<html lang="en">
<head>
<meta charset="utf-8">
<title>The Merry Hound – Business Card</title>
<link href="https://fonts.googleapis.com/css2?family=Mulish:wght@300;400;700&display=swap" rel="stylesheet">
<style>
  :root {
    --page: #ececec;
    --card-blue: #afcde6;
    --stripe-blue: #a6c8e5;
    --white: #ffffff;
    --grey: #757575;
    --ink: #333333;
    --name-blue: #1c7fc9;
    --icon-blue: #3f8fd2;
  }
  * { box-sizing: border-box; margin: 0; padding: 0; }
  html, body {
    width: 1200px; height: 434px; overflow: hidden;
    background: var(--page);
    font-family: "Mulish", sans-serif;
  }
  .sheet {
    position: relative; width: 1200px; height: 434px;
    display: flex; gap: 40px; justify-content: center; align-items: center;
  }
  .card {
    position: relative; width: 560px; height: 320px; overflow: hidden;
    box-shadow: 0 4px 14px rgba(0,0,0,.18);
  }

  /* Front */
  .card--front { background: var(--card-blue); }
  .front-brand {
    position: absolute; left: 0; right: 0; top: 118px; text-align: center;
  }
  .front-brand__name {
    font-weight: 300; font-size: 46px; color: var(--white); letter-spacing: 1px;
    line-height: 1;
  }
  .front-brand__tagline {
    margin-top: 12px; font-weight: 400; font-size: 11px; color: var(--white);
    letter-spacing: 3.2px; text-transform: uppercase;
  }

  /* Back */
  .card--back { background: var(--white); }
  .back-panel {
    position: absolute; left: 0; top: 0; width: 248px; height: 100%;
    background: var(--card-blue);
  }
  .back-stripes { position: absolute; left: 248px; top: 0; height: 100%; width: 30px; }
  .back-brand {
    position: absolute; left: 0; width: 248px; top: 112px; text-align: center;
  }
  .back-brand__name {
    font-weight: 300; font-size: 36px; color: var(--grey); line-height: 1.05;
  }
  .back-brand__mark {
    display: inline-block; width: 12px; height: 12px; border-radius: 50%;
    background: var(--grey); margin-top: 12px;
  }
  .person {
    position: absolute; right: 22px; top: 40px; text-align: right;
  }
  .person__name { font-weight: 700; font-size: 18px; color: var(--name-blue); letter-spacing: .5px; }
  .person__role { font-weight: 400; font-size: 11px; color: var(--ink); margin-top: 4px; }
  .contacts {
    position: absolute; right: 18px; bottom: 30px; width: 264px; list-style: none;
  }
  .contacts li {
    display: flex; align-items: center; justify-content: flex-end; gap: 6px;
    font-size: 10.5px; font-weight: 700; color: var(--ink); height: 24px;
    white-space: nowrap;
  }
  .contacts svg { width: 17px; height: 17px; flex: none; }
</style>
</head>
<body>
  <main class="sheet">
    <section class="card card--front" aria-label="Card front">
      <div class="front-brand">
        <div class="front-brand__name">The Merry Hound</div>
        <div class="front-brand__tagline">Positive Training Specialist</div>
      </div>
    </section>

    <section class="card card--back" aria-label="Card back">
      <div class="back-panel"></div>
      <svg class="back-stripes" viewBox="0 0 30 320" preserveAspectRatio="none" aria-hidden="true">
        <rect x="0" y="0" width="6" height="320" fill="var(--white)"/>
        <rect x="6" y="0" width="7" height="320" fill="var(--stripe-blue)"/>
        <rect x="13" y="0" width="5" height="320" fill="var(--white)"/>
        <rect x="18" y="0" width="7" height="320" fill="var(--stripe-blue)"/>
      </svg>
      <div class="back-brand">
        <div class="back-brand__name">The Merry<br>Hound</div>
        <span class="back-brand__mark"></span>
      </div>

      <div class="person">
        <div class="person__name">Miriam Caslett</div>
        <div class="person__role">Trained Professional Dog Trainer</div>
      </div>

      <ul class="contacts">
        <li>0499731628
          <svg viewBox="0 0 18 18" aria-label="Phone"><rect x="1" y="1" width="16" height="16" rx="2" fill="none" stroke="var(--icon-blue)" stroke-width="1.5"/><rect x="6" y="4" width="6" height="10" rx="1" fill="var(--icon-blue)"/></svg>
        </li>
        <li>miriam@themerryhound-example.com.au
          <svg viewBox="0 0 18 18" aria-label="Email"><rect x="1" y="1" width="16" height="16" rx="2" fill="none" stroke="var(--icon-blue)" stroke-width="1.5"/><rect x="4" y="5.5" width="10" height="7" fill="var(--icon-blue)"/><path d="M4 5.5 L9 9.5 L14 5.5" fill="none" stroke="var(--white)" stroke-width="1"/></svg>
        </li>
        <li>www.themerryhound-example.com.au
          <svg viewBox="0 0 18 18" aria-label="Website"><rect x="1" y="1" width="16" height="16" rx="2" fill="none" stroke="var(--icon-blue)" stroke-width="1.5"/><circle cx="9" cy="9" r="4.5" fill="none" stroke="var(--icon-blue)" stroke-width="1.3"/><path d="M4.5 9 H13.5 M9 4.5 V13.5" stroke="var(--icon-blue)" stroke-width="1"/></svg>
        </li>
      </ul>
    </section>
  </main>
</body>
</html>
```